Yacht, Boats, Watersports company needs a redesign of business card

Hello Designers!
We are a Boat dealership company that sells fun in the water, we sell boats, Yachts, Kayaks and also yacht WaterSport toys. We are looking to redesign our business cards in to something a little bit more sophisticated. in a way that we can make better use of our company colors. I'm attaching a zipped file containing the company 3 sets of company logo which one is an horizontal another one is a vertical and also a chromed 3d logo. Also is included two set of business cards that we use and also some designs that i think it's interesting. We use PMS 2026c Orange and PMS 7687C Blue. I would like to see at least two different options with the orange as accent and also using blue as an accent color. It's really important for the business cards to have a font option and size that is legible to most people. Our current website is wwww.corvellamarine.com. Please visit if you want to have a better feeling of the Boat dealership
You can send Single sided or double side options. We are now using single sided but we may be open for a double side option if we really like the design.
Target Market(s)
Marine, boat sales, yacht sales, water toys sales/
Contact Information for Business Card
Name: Dale Pritchett
Address: 718 West Halden Lane,
Port Calloway, GA 31520
Phone: 954-382-7146
Fax: 954:382-7139
Cell: 954-451-8320
Email: 212@corvellamarine.com
Website: corvellamarine.com
Requirements
Must have
- the current information of the business card provided.
logo
use the PMS Colors
Nice to have
- a touch of elegance and sophistication but simple
Should not have
- should not have any typography that is hard to read, the card should be simple but yet sophisticated.

```html
<!DOCTYPE html>
<html lang="en">
<head>
<meta charset="utf-8">
<title>Corvella Marine – Business Card</title>
<link rel="stylesheet" href="https://fonts.googleapis.com/css2?family=Montserrat:wght@800&family=Roboto:wght@400;500&family=Roboto+Condensed:wght@700&display=swap">
<style>
  :root {
    --blue: #1756a4;
    --orange: #ef7124;
    --bleed: #b3b3b3;
    --white: #ffffff;
    --ink: #222222;
  }
  * { box-sizing: border-box; margin: 0; padding: 0; }
  html, body { width: 1200px; height: 1200px; overflow: hidden; background: var(--white); }
  .canvas { position: relative; width: 1200px; height: 1200px; font-family: "Roboto", Arial, sans-serif; }

  .bleed-area { position: absolute; background: var(--bleed); }
  .bleed-label { position: absolute; font-size: 11px; color: var(--ink); font-family: Arial, sans-serif; }
  .bleed-label.vertical { transform: rotate(90deg); transform-origin: left top; }

  /* Front */
  .front { left: 147px; top: 153px; width: 560px; height: 337px; }
  .front-card { position: absolute; left: 18px; top: 20px; width: 523px; height: 297px; background: var(--white); border-radius: 31px; }
  .front-band { position: absolute; left: 0; width: 560px; }
  .front-band.blue { top: 56px; height: 21px; background: var(--blue); }
  .front-band.orange { top: 260px; height: 19px; background: var(--orange); }
  .brand-mark { position: absolute; left: 235px; top: 101px; width: 90px; height: 90px; border-radius: 50%; background: var(--blue); }
  .brand-name {
    position: absolute; left: 0; right: 0; top: 204px; text-align: center; white-space: nowrap;
    font-family: "Montserrat", Arial, sans-serif; font-weight: 800; font-size: 35px;
    letter-spacing: 1.5px; color: var(--blue);
  }
  .front-web {
    position: absolute; left: 0; right: 0; top: 287px; text-align: center;
    font-size: 15px; letter-spacing: 3px; color: var(--blue);
  }
  .front-web .accent { color: var(--orange); }

  /* Back */
  .back { left: 547px; top: 758px; width: 558px; height: 337px; }
  .back-head {
    position: absolute; left: 17px; top: 20px; width: 525px; height: 85px;
    background: var(--blue); border-radius: 31px 31px 0 0; text-align: center;
  }
  .holder-name {
    margin-top: 21px; font-family: "Roboto Condensed", Arial, sans-serif; font-weight: 700;
    font-size: 21px; color: var(--white); letter-spacing: 0.5px;
  }
  .holder-title { margin-top: 2px; font-size: 11px; letter-spacing: 3.5px; color: var(--orange); font-weight: 500; }
  .back-body {
    position: absolute; left: 17px; top: 126px; width: 525px; height: 192px;
    background: var(--orange); border-radius: 0 0 31px 31px;
  }
  .contact-list { position: absolute; left: 35px; top: 17px; list-style: none; }
  .contact-item { position: relative; padding-left: 31px; color: var(--white); font-size: 14px; line-height: 17px; }
  .contact-item + .contact-item { margin-top: 16px; }
  .contact-icon { position: absolute; left: 0; top: 50%; width: 24px; height: 24px; margin-top: -12px; }
  .divider { position: absolute; left: 351px; top: 25px; width: 1px; height: 144px; background: rgba(255,255,255,0.8); }
  .social { position: absolute; left: 405px; top: 76px; display: flex; gap: 8px; }
  .social span { width: 20px; height: 20px; border-radius: 50%; background: var(--white); }
  .social span:first-child { background: var(--blue); border-radius: 3px; }
</style>
</head>
<body>
<div class="canvas">

  <section class="bleed-area front" aria-label="Card front">
    <div class="front-card"></div>
    <div class="front-band blue"></div>
    <div class="front-band orange"></div>
    <div class="brand-mark"></div>
    <div class="brand-name">CORVELLA MARINE</div>
    <div class="front-web">www.corvella<span class="accent">marine</span>.com</div>
  </section>
  <span class="bleed-label vertical" style="left:161px; top:290px;">bleed</span>
  <span class="bleed-label" style="left:345px; top:476px;">bleed</span>

  <section class="bleed-area back" aria-label="Card back">
    <header class="back-head">
      <div class="holder-name">DALE PRITCHETT</div>
      <div class="holder-title">CORPORATE MANAGER</div>
    </header>
    <div class="back-body">
      <ul class="contact-list">
        <li class="contact-item">
          <svg class="contact-icon" viewBox="0 0 24 24"><circle cx="12" cy="12" r="12" fill="#fff"/><path d="M7 9c0-1.5 2-2.5 5-2.5s5 1 5 2.5l-2 1-1-1.5h-4l-1 1.5z M8 12h8l1 5H7z" fill="#ef7124"/></svg>
          1.555.382.7146<br>1.555.451.8320
        </li>
        <li class="contact-item">
          <svg class="contact-icon" viewBox="0 0 24 24"><circle cx="12" cy="12" r="12" fill="#fff"/><rect x="9" y="6" width="6" height="4" fill="#ef7124"/><rect x="6" y="10" width="12" height="5" rx="1" fill="#ef7124"/><rect x="9" y="14" width="6" height="4" fill="#ef7124"/></svg>
          1.555.382.7139
        </li>
        <li class="contact-item">
          <svg class="contact-icon" viewBox="0 0 24 24"><circle cx="12" cy="12" r="12" fill="#fff"/><path d="M12 6l6 5.5h-2V17h-3v-3.5h-2V17H8v-5.5H6z" fill="#ef7124"/></svg>
          718 West Halden Lane<br>Port Calloway, GA 31520
        </li>
        <li class="contact-item">
          <svg class="contact-icon" viewBox="0 0 24 24"><circle cx="12" cy="12" r="12" fill="#fff"/><g fill="none" stroke="#ef7124" stroke-width="1.3"><circle cx="12" cy="12" r="6"/><ellipse cx="12" cy="12" rx="2.5" ry="6"/><path d="M6 12h12M7 9h10M7 15h10"/></g></svg>
          212@corvellamarine.com
        </li>
      </ul>
      <div class="divider"></div>
      <div class="social" aria-label="Social media"><span></span><span></span><span></span></div>
    </div>
  </section>
  <span class="bleed-label vertical" style="left:559px; top:951px;">bleed</span>
  <span class="bleed-label" style="left:748px; top:1079px;">bleed</span>

</div>
</body>
</html>
```